Dental Magazine Cover

I need a template created for a magazine cover. Magazine title is "Dentistry Halvern"

I would like to have a logo designed for "Dentistry Halvern"

For each issue, we would like to keep the same basic template and change out the photos, text, etc. according to the contents of the issue.

You can create the cover of the first issue with the attached photos and captions:

Date for use on magazine cover is February 2014

Main caption: Maxillary Reconstruction with Immediately Loaded Dental Implants
(Use attached File 1 for main photo. Photo may be cropped and rotated as needed)

Inset: Bisphosphonate Guidelines for Dental Treatment
(Use attached file 2 for inset photo. Photo may be cropped and rotated as needed).

Target Market(s)

Target audience for this magazine are dentists, dental hygienists, dental assistants, and dental professionals in the Austin, Texas area.

Industry/Entity Type

Dental

Other font styles liked:
• Font need to "POP"

Requirements
Must have
• Please see project overview guidelines. Magazine cover needs to have the following:
1) Logo
2) Main image
3) Caption for Main image (Maxillary Reconstruction with Immediately Loaded Dental Implants)
4) Smaller Inset Photo
5) Caption for smaller inset photo (Bisphosphonate Guidelines for Dental Treatment)
6) Date of magazine issue (February 2014)

Use any of the Photos you see fit to make the magazine cover work.
Nice to have
• Please try to make the "Dentistry Halvern" logo "POP". Dental journals are boring enough. We can at least have a logo that pops. Simply using generic text will win this design. The below text is just a suggestion of a Logo. Please feel free to use all creative license in making a logo that has some sizzle. PLEASE NOTE: A tooth is NOT needed in the logo...

```html
<!DOCTYPE html>
<html lang="en">
<head>
<meta charset="utf-8">
<title>Dentistry Halvern — February 2014</title>
<link rel="stylesheet" href="https://fonts.googleapis.com/css2?family=Bebas+Neue&family=Roboto+Slab:wght@300;400&display=swap">
<style>
  :root {
    --page: #ffffff;
    --sky: #00aeef;
    --navy: #0067a3;
    --navy-deep: #005a91;
    --ink: #050505;
    --white: #ffffff;
    --caption-blue: #1aa6e6;
  }
  * { margin: 0; padding: 0; box-sizing: border-box; }
  html, body {
    width: 1200px; height: 1000px; overflow: hidden;
    background: var(--page);
  }
  .cover {
    position: absolute; left: 300px; top: 85px;
    width: 601px; height: 801px;
    background: var(--white);
    border: 1px solid #222;
    overflow: hidden;
  }
  .masthead {
    position: absolute; left: 0; top: 0; width: 100%; height: 198px;
    background: var(--sky);
  }
  .issue-line {
    position: absolute; left: 41px; top: 22px;
    font: 400 13px/1 "Bebas Neue", sans-serif;
    letter-spacing: 3.2px; color: var(--white);
  }
  .title-mark { position: absolute; left: 0; top: 0; }
  .title-mark text {
    font-family: "Bebas Neue", sans-serif;
    fill: var(--white);
  }
  .feature {
    position: absolute; left: 0; top: 206px; width: 100%; height: 446px;
    background: var(--ink);
  }
  .feature-photo {
    position: absolute; left: 0; top: 0; width: 100%; height: 250px;
    background:
      radial-gradient(ellipse 55% 45% at 50% 65%, #d9d6cf 0%, #8a6f62 35%, rgba(60,40,30,0.6) 60%, rgba(5,5,5,0) 80%),
      linear-gradient(180deg, #3a3128 0%, #050505 100%);
  }
  .feature-caption {
    position: absolute; right: 42px; top: 278px;
    text-align: right;
    font-family: "Roboto Slab", serif; font-weight: 300;
    text-transform: uppercase;
  }
  .feature-caption .lead {
    display: block; color: var(--white);
    font-size: 38px; line-height: 40px; letter-spacing: 1px;
  }
  .feature-caption .sub {
    display: block; color: var(--caption-blue);
    font-size: 29px; line-height: 32px; letter-spacing: 1px;
  }
  .feature-caption .sub:first-of-type { margin-top: 2px; }
  .inset-band {
    position: absolute; left: 0; top: 659px; width: 100%; height: 142px;
    background: linear-gradient(180deg, var(--navy) 0%, var(--navy-deep) 100%);
  }
  .inset-photo {
    position: absolute; left: 43px; top: 0;
    width: 138px; height: 112px;
    border: 4px solid var(--white); border-top: 0;
    border-bottom-right-radius: 30px;
    background: linear-gradient(135deg, #2a1e2e 0%, #7a6b9c 30%, #e6e0d6 50%, #3f8f7a 70%, #1a1a1a 100%);
  }
  .inset-caption {
    position: absolute; left: 211px; top: 38px;
    font: 300 19px/25px "Roboto Slab", serif;
    letter-spacing: 1.4px; color: var(--white);
    text-transform: uppercase;
  }
</style>
</head>
<body>
  <main class="cover">
    <header class="masthead">
      <p class="issue-line">Dentistry Halvern • February 2014</p>
      <svg class="title-mark" width="601" height="198" viewBox="0 0 601 198" aria-label="Dentistry Halvern">
        <text x="41" y="163" font-size="172" textLength="518" lengthAdjust="spacingAndGlyphs">DENTISTRY</text>
        <text x="558" y="190" font-size="30" text-anchor="end" letter-spacing="2">HALVERN</text>
      </svg>
    </header>

    <section class="feature">
      <div class="feature-photo" role="img" aria-label="Photograph of a full upper-jaw implant prosthesis on a stone model, lit against black"></div>
      <h1 class="feature-caption">
        <span class="lead">Maxillary</span>
        <span class="lead">Reconstruction</span>
        <span class="sub">with Immediately</span>
        <span class="sub">Loaded Dental Implants</span>
      </h1>
    </section>

    <section class="inset-band">
      <div class="inset-photo" role="img" aria-label="Colour micrograph of trabecular bone structure"></div>
      <h2 class="inset-caption">Bisphosphonate Guidelines<br>for Dental Treatment</h2>
    </section>
  </main>
</body>
</html>
```